Website for a Construction Business That Builds Houses

We want some design concepts for this website. Customer likes this competitor site: https://brenwickdwellings.com.au/

We have a logo for Tarvond Constructions. Logo font is Birdman, attached with AI.

Want to be able to change hero images

Will have a contact page.

Need to know what plugins will be used for WordPress.

Coding

Coded - Design and coding required

```html
<!DOCTYPE html>
<html lang="en">
<head>
<meta charset="utf-8">
<title>Tarvond Constructions — Home Designs</title>
<link href="https://fonts.googleapis.com/css2?family=Gloock&family=Figtree:wght@400;500;600;700&display=swap" rel="stylesheet">
<style>
:root{
  --navy:#063447;
  --navy-deep:#04222e;
  --green:#8dc63f;
  --ink:#0b3a4d;
  --grey:#6b6f73;
  --field:#d9d9d9;
  --white:#ffffff;
}
*{box-sizing:border-box;margin:0;padding:0}
html,body{width:1200px;height:2923px;overflow:hidden;background:var(--white)}
body{position:relative;font-family:"Figtree",sans-serif;color:var(--ink)}
.abs{position:absolute}
.serif{font-family:"Gloock",serif;font-weight:400}
.eyebrow{font-size:11px;font-weight:700;letter-spacing:1.6px;text-transform:uppercase}
.link-arrow{display:inline-flex;align-items:center;gap:6px;font-size:10.5px;font-weight:700;letter-spacing:1.2px;text-transform:uppercase;border-bottom:1.5px solid currentColor;padding-bottom:3px}
.btn{background:var(--green);color:var(--white);display:flex;align-items:center;justify-content:center;gap:6px;font-size:10.5px;font-weight:700;letter-spacing:1.3px;text-transform:uppercase}

/* header */
.site-header{left:0;top:0;width:1200px;height:88px;background:var(--navy)}
.topbar{left:188px;top:0;width:830px;height:25px;display:flex;align-items:center;gap:18px;font-size:9px;color:#e4edf0;border-bottom:1px solid rgba(255,255,255,.25)}
.topbar span{display:flex;align-items:center;gap:6px}
.socials-top{right:183px;top:6px;display:flex;gap:5px}
.socials-top i{width:11px;height:11px;border:1px solid #e4edf0;border-radius:50%;display:block}
.brand{left:188px;top:41px;display:flex;align-items:center;gap:8px;color:var(--white);font-size:17px;font-weight:600}
.brand i{width:24px;height:24px;border-radius:50%;background:var(--green);display:block}
.nav{left:448px;top:46px;display:flex;gap:16px;font-size:12.5px;font-weight:600;color:var(--white)}
.nav .active{color:var(--green);border-bottom:2px solid var(--green);padding:0 4px 4px}
.nav-cta{left:900px;top:40px;width:118px;height:28px}

/* hero */
.hero-image{left:0;top:88px;width:1200px;height:497px;background:linear-gradient(180deg,#4e7884 0%,#6d8f98 55%,#b8c8cc 100%)}
.hero-title{left:0;top:240px;width:1200px;text-align:center;font-size:46px;line-height:53px;color:var(--white);letter-spacing:.5px}
.hero-text{left:320px;top:360px;width:560px;text-align:center;font-size:10.5px;line-height:15px;color:var(--white)}

/* mission */
.mission-label{left:192px;top:652px;color:var(--grey)}
.mission-title{left:192px;top:675px;font-size:20px;line-height:24px;color:var(--ink)}
.mission-text{left:192px;top:740px;width:520px;font-size:10.5px;line-height:15px;color:var(--grey)}
.mission-btn{left:886px;top:741px;width:138px;height:37px}
.card{top:826px;width:266px;height:373px}
.card-one{left:192px;background:linear-gradient(180deg,#6f919d 0%,#2e5b6c 60%,#0f3a4b 100%)}
.card-two{left:474px;background:linear-gradient(180deg,#eef0f0 0%,#c7d3d2 50%,#9c8a74 100%)}
.card-three{left:756px;background:linear-gradient(180deg,#f3f3f2 0%,#d5d5d3 55%,#a9a8a5 100%)}
.card-caption{left:192px;top:1106px;width:266px;text-align:center;font-size:17px;color:var(--green)}
.card-more{left:287px;top:1145px;color:var(--white)}

/* features */
.feature-text{width:595px;height:347px;background:var(--navy-deep)}
.feature-photo{width:605px;height:347px;background:linear-gradient(180deg,#2a2826 0%,#6b4a2a 45%,#7d7a76 100%)}
.feature-photo.stairs{width:595px;background:linear-gradient(90deg,#8a5a2c 0%,#2c2a28 30%,#3a332c 60%,#9a6a34 80%,#2c2a28 100%)}
.f-eyebrow{color:var(--white)}
.f-title{font-size:20px;line-height:24px;color:var(--green)}
.f-body{font-size:10.5px;line-height:15.2px;color:var(--white);letter-spacing:.25px}
.f-link{color:var(--green)}

/* enquiry */
.enquiry-band{left:0;top:2628px;width:1200px;height:295px;background:var(--navy)}
.enquiry-card{left:182px;top:2380px;width:842px;height:324px;background:var(--white);box-shadow:0 4px 18px rgba(0,0,0,.12)}
.field{background:var(--field);color:#8a8d90;font-size:10.5px;padding:9px 10px}
.map{left:724px;top:2407px;width:284px;height:274px;background:linear-gradient(160deg,#f1f1f1 0%,#e3e3e3 55%,#a9a9a9 100%)}

/* footer */
.foot-brand{left:186px;top:2790px;display:flex;align-items:center;gap:8px;color:var(--white);font-size:15px;font-weight:600}
.foot-brand i{width:26px;height:26px;border-radius:50%;background:var(--green);display:block}
.foot-h{font-size:15px;color:var(--green);text-transform:uppercase}
.foot-text{left:333px;top:2808px;width:210px;font-size:10.5px;line-height:15px;color:var(--white)}
.foot-nav{left:625px;top:2808px;display:flex;gap:14px;font-size:11px;font-weight:600;color:var(--white)}
.foot-social{left:626px;top:2828px;display:flex;gap:8px}
.foot-social i{width:17px;height:17px;border:1.3px solid var(--white);border-radius:50%;display:block}
</style>
</head>
<body>

<header class="site-header abs">
  <div class="topbar abs">
    <span><svg width="10" height="10" viewBox="0 0 10 10"><path d="M2 1l2 2-1 1.5c.6 1.2 1.3 1.9 2.5 2.5L7 6l2 2-1.5 1.5C4 9 1 6 .5 2.5z" fill="#8dc63f"/></svg>(02) 9000 4417</span>
    <span><svg width="11" height="8" viewBox="0 0 11 8"><rect x=".5" y=".5" width="10" height="7" fill="none" stroke="#8dc63f"/><path d="M.5.5l5 4 5-4" fill="none" stroke="#8dc63f"/></svg>hello@tarvond.com</span>
    <span><svg width="8" height="11" viewBox="0 0 8 11"><path d="M4 0a4 4 0 014 4c0 3-4 7-4 7S0 7 0 4a4 4 0 014-4z" fill="#8dc63f"/><circle cx="4" cy="4" r="1.4" fill="#063447"/></svg>48 Harlow Lane, New South Wales</span>
  </div>
  <div class="socials-top abs"><i></i><i></i><i></i></div>
  <div class="brand abs"><i></i>Tarvond</div>
  <nav class="nav abs">
    <span class="active">Home Designs</span><span>Display Homes</span><span>Custom Build</span><span>Knock Down Rebuild</span>
  </nav>
  <div class="nav-cta btn abs">Contact <span>&rarr;</span></div>
</header>

<section>
  <div class="hero-image abs" role="img" aria-label="Bright open-plan kitchen and living room with a navy tint"></div>
  <h1 class="hero-title serif abs">Personalize your home with<br>our creative design team.</h1>
  <p class="hero-text abs">Experience the perfect blend of elegance and affordability with our carefully curated spaces designed to meet the highest standards of style and comfort. Whether you're looking to enhance your home or business environment.</p>
</section>

<section>
  <div class="mission-label eyebrow abs">Our missSion.</div>
  <h2 class="mission-title serif abs">Discover the joy of your dream<br>home with us...</h2>
  <p class="mission-text abs">Experience the perfect blend of elegance and affordability with our carefully curated spaces designed to meet the highest standards of style and comfort. Whether you're looking to enhance your home or business environment.</p>
  <div class="mission-btn btn abs">More about us <span>&rarr;</span></div>

  <div class="card card-one abs" role="img" aria-label="Modern white kitchen with navy overlay"></div>
  <div class="card card-two abs" role="img" aria-label="Dining room with timber table and pendant lights"></div>
  <div class="card card-three abs" role="img" aria-label="Open kitchen with rattan pendant lights"></div>
  <div class="card-caption serif abs">Our houseing project</div>
  <div class="card-more link-arrow abs">Read more <span>&rarr;</span></div>
</section>

<section>
  <div class="feature-text abs" style="left:0;top:1300px"></div>
  <div class="feature-photo abs" style="left:595px;top:1300px" role="img" aria-label="Dark kitchen with timber cabinetry and lit splashback"></div>
  <div class="f-eyebrow eyebrow abs" style="left:181px;top:1386px">Unveil the beauty</div>
  <h3 class="f-title serif abs" style="left:181px;top:1410px">Unveil the beauty of our<br>exclusive homes.</h3>
  <p class="f-body abs" style="left:181px;top:1466px;width:366px">Welcome to a world where every detail is crafted to perfection. Unveil the beauty of our exclusive homes, where luxury meets sophistication and each space is thoughtfully designed to inspire. From the finest materials to the most elegant finishes, our homes are a testament to unparalleled quality and timeless elegance.</p>
  <div class="f-link link-arrow abs" style="left:182px;top:1555px">Read more <span>&rarr;</span></div>

  <div class="feature-photo stairs abs" style="left:0;top:1647px" role="img" aria-label="Hallway with timber wall panels and lit timber staircase"></div>
  <div class="feature-text abs" style="left:595px;top:1647px;width:605px"></div>
  <div class="f-eyebrow eyebrow abs" style="left:657px;top:1733px">Personalize dream home</div>
  <h3 class="f-title serif abs" style="left:657px;top:1757px">Personalize your dream home with<br>our creative design team.</h3>
  <p class="f-body abs" style="left:657px;top:1813px;width:366px">Your dream home is a reflection of your unique style and vision, and we're here to bring it to life. With our creative design team by your side, you have the freedom to personalize every detail, ensuring that your home is truly one-of-a-kind. From selecting the perfect color palettes to customizing floor plans and finishes, our experts work closely with you to turn your ideas into reality.</p>
  <div class="f-link link-arrow abs" style="left:658px;top:1917px">Read more <span>&rarr;</span></div>

  <div class="feature-text abs" style="left:0;top:1993px"></div>
  <div class="feature-photo abs" style="left:595px;top:1993px" role="img" aria-label="Dark kitchen with timber cabinetry and lit splashback"></div>
  <div class="f-eyebrow eyebrow abs" style="left:181px;top:2079px">Unveil the beauty</div>
  <h3 class="f-title serif abs" style="left:181px;top:2103px">Unveil the beauty of our<br>exclusive homes.</h3>
  <p class="f-body abs" style="left:181px;top:2159px;width:366px">Welcome to a world where every detail is crafted to perfection. Unveil the beauty of our exclusive homes, where luxury meets sophistication and each space is thoughtfully designed to inspire. From the finest materials to the most elegant finishes, our homes are a testament to unparalleled quality and timeless elegance.</p>
  <div class="f-link link-arrow abs" style="left:182px;top:2248px">Read more <span>&rarr;</span></div>
</section>

<section>
  <div class="enquiry-band abs"></div>
  <div class="enquiry-card abs"></div>
  <div class="eyebrow abs" style="left:218px;top:2435px;color:var(--grey)">Quick enquiry.</div>
  <h2 class="serif abs" style="left:218px;top:2459px;font-size:20px;color:var(--ink)">Want more information?</h2>
  <div class="field abs" style="left:216px;top:2500px;width:249px;height:28px">Your name</div>
  <div class="field abs" style="left:474px;top:2500px;width:226px;height:28px">Your email</div>
  <div class="field abs" style="left:216px;top:2539px;width:484px;height:80px">Message</div>
  <div class="btn abs" style="left:216px;top:2631px;width:149px;height:33px">Send message <span>&rarr;</span></div>
  <div class="map abs" role="img" aria-label="Street map of the city and bay area"></div>
</section>

<footer>
  <div class="foot-brand abs"><i></i>Tarvond</div>
  <div class="foot-h serif abs" style="left:333px;top:2772px">Contact us</div>
  <p class="foot-text abs">Our team is dedicated to making your home-building journey as smooth and enjoyable as possible.</p>
  <div class="foot-h serif abs" style="left:627px;top:2772px">Navigation</div>
  <div class="foot-nav abs"><span>Home Designs</span><span>Display Homes</span><span>Custom Build</span><span>Knock Down Rebuild</span></div>
  <div class="foot-social abs"><i></i><i></i><i></i></div>
</footer>

</body>
</html>
```